Trade Show Display Design For A Real Estate Lending Company

We are in need of an impactful and modern trade show booth design that is consistent with the new branding and imagery found on our website www.qvt7.net.

Established in 2010, Crestmoor Funding Partners, LLC is a Hard Money Lender providing fast bridge financing to real estate investors for the purchase, renovation, or new construction of single family, multi-family and mixed use properties. We have closed over 800 loans since we began with total transaction amounts in excess of $170 million.

We like to stress that we are local lenders, and our lending area includes NJ, NY, CT, MA, PA, FL, MD, VA, DC. In addition, one of our major differentiators is that we close loans extremely fast.
Here is what we need for this project, and the artwork templates are attached.

-1 backdrop display design
-1 countertop wrap design
-1 retractable banner design

The backdrop display and the countertop will be used together. The retractable banner will be used together with the backdrop and by itself.

Target Market(s)

Real estate agents, mortgage brokers, builders, and other real estate investors.

Industry/Entity Type

Real Estate

Font styles to use
Other font styles liked:
• Proxima Nova and Roboto Slab (or similar)

Requirements
Must have
• Must include a design for all three elements (backdrop, retractable banner, counter top). Final submission must also be submitted using the print-ready art templates provided.

```html
<!DOCTYPE html>
<html lang="en">
<head>
<meta charset="utf-8">
<title>Crestmoor Funding Partners — Trade Show Display Set</title>
<link rel="stylesheet" href="https://fonts.googleapis.com/css2?family=Open+Sans:wght@400;600;700;800&display=swap">
<style>
  :root {
    --sheet: #ffffff;
    --label: #222222;
    --teal-dark: #1f5f6b;
    --band-start: #2a7468;
    --band-end: #3b8c7c;
    --band-text: #ffffff;
    --green: #48ad68;
    --mint: #d6ebe3;
    --mint-deep: #bcd9cf;
    --peach: #f1d4bd;
    --sage: #cfe2d6;
  }
  * { margin: 0; padding: 0; box-sizing: border-box; }
  html, body { width: 885px; height: 1200px; overflow: hidden; }
  body {
    position: relative;
    background: var(--sheet);
    font-family: "Open Sans", Arial, sans-serif;
  }
  .piece-label {
    position: absolute;
    font-size: 15px;
    color: var(--label);
    font-weight: 400;
  }
  .piece {
    position: absolute;
    overflow: hidden;
  }
  .piece-bg {
    position: absolute; inset: 0;
    background:
      radial-gradient(ellipse at 70% 80%, rgba(241,212,189,0.9) 0%, rgba(241,212,189,0) 55%),
      radial-gradient(ellipse at 20% 65%, rgba(238,206,184,0.75) 0%, rgba(238,206,184,0) 45%),
      radial-gradient(ellipse at 80% 15%, rgba(188,217,207,0.9) 0%, rgba(188,217,207,0) 50%),
      linear-gradient(160deg, var(--mint) 0%, var(--sage) 45%, var(--mint-deep) 100%);
  }
  .brand {
    position: absolute;
    display: flex;
    align-items: center;
    gap: 6px;
    color: var(--green);
    font-weight: 700;
    text-transform: uppercase;
    line-height: 1.1;
  }
  .brand-mark { background: var(--green); flex: none; }
  .contact {
    position: absolute;
    color: var(--green);
    font-weight: 700;
    line-height: 1.2;
  }
  .band {
    position: absolute; left: 0; right: 0;
    background: linear-gradient(90deg, var(--band-start), var(--band-end) 50%, var(--band-start));
    color: var(--band-text);
    font-weight: 700;
    display: flex; align-items: center; justify-content: center;
    text-align: center;
    line-height: 1.25;
  }
  .stat-number {
    position: absolute;
    color: var(--teal-dark);
    font-weight: 800;
    line-height: 1;
  }
  .stat-label {
    position: absolute;
    color: var(--green);
    font-weight: 700;
    text-transform: uppercase;
    line-height: 1.2;
  }
  .lend-box {
    position: absolute;
    border: 3px solid var(--teal-dark);
  }
  .lend-title {
    color: var(--teal-dark);
    font-weight: 800;
    text-transform: uppercase;
  }
  .state-list {
    list-style: none;
    color: var(--green);
    font-weight: 600;
  }
</style>
</head>
<body>

  <!-- Backdrop -->
  <p class="piece-label" style="left:383px; top:2px;">Backdrop</p>
  <section class="piece backdrop" style="left:0; top:33px; width:885px; height:505px;">
    <div class="piece-bg" role="img" aria-label="Soft faceted background in mint green and peach tones"></div>
    <div class="brand" style="left:112px; top:60px; font-size:14px;">
      <span class="brand-mark" style="width:14px; height:14px;"></span>
      <span>Crestmoor Funding<br>Partners, LLC</span>
    </div>
    <div class="contact" style="left:594px; top:58px; font-size:19px;">555.018.4420<br>info@qvt7.net</div>
    <div class="band" style="top:134px; height:72px; font-size:37px; letter-spacing:0.3px;">WE CLOSE LOANS EXTREMELY FAST</div>
    <div class="stat-number" style="left:110px; top:252px; font-size:55px;">725+</div>
    <div class="stat-label" style="left:330px; top:265px; width:113px; text-align:right; font-size:14px;">Project<br>Funded</div>
    <div class="stat-number" style="left:110px; top:357px; font-size:55px;">170 MM</div>
    <div class="stat-label" style="left:330px; top:370px; width:113px; text-align:right; font-size:14px;">Loans<br>Made</div>
    <div class="lend-box" style="left:576px; top:248px; width:154px; height:217px; padding:14px 0 0 30px;">
      <p class="lend-title" style="font-size:15px; margin-bottom:12px;">We Lend In</p>
      <ul class="state-list" style="font-size:14px; line-height:18.5px;">
        <li>New Jersey</li><li>New York</li><li>Florida</li><li>Maryland</li>
        <li>Massachusetts</li><li>Connecticut</li><li>Pennsylvania</li><li>Virginia and D.C.</li>
      </ul>
    </div>
  </section>

  <!-- Retractable banner -->
  <p class="piece-label" style="left:45px; top:595px;">Retractable banner</p>
  <section class="piece banner" style="left:0; top:638px; width:242px; height:562px;">
    <div class="piece-bg" role="img" aria-label="Soft faceted background in mint green and peach tones"></div>
    <div class="brand" style="left:12px; top:24px; font-size:8px;">
      <span class="brand-mark" style="width:9px; height:9px;"></span>
      <span>Crestmoor Funding<br>Partners, LLC</span>
    </div>
    <div class="contact" style="left:152px; top:24px; font-size:11px;">555.018.4420<br>info@qvt7.net</div>
    <div class="band" style="top:97px; height:65px; font-size:20px;">WE CLOSE LOANS<br>EXTREMELY FAST</div>
    <div class="stat-number" style="left:24px; top:200px; font-size:26px;">725+</div>
    <div class="stat-label" style="left:18px; top:231px; width:68px; text-align:center; font-size:10px;">Project<br>Funded</div>
    <div class="stat-number" style="left:124px; top:200px; font-size:26px;">170 MM</div>
    <div class="stat-label" style="left:136px; top:231px; width:68px; text-align:center; font-size:10px;">Loans<br>Made</div>
    <div class="lend-box" style="left:55px; top:311px; width:129px; height:157px; padding:10px 0 0 0; text-align:center;">
      <p class="lend-title" style="font-size:12px; margin-bottom:8px;">We Lend In</p>
      <ul class="state-list" style="font-size:11px; line-height:14.5px;">
        <li>New Jersey</li><li>New York</li><li>Florida</li><li>Maryland</li>
        <li>Massachusetts</li><li>Connecticut</li><li>Pennsylvania</li><li>Virginia and D.C</li>
      </ul>
    </div>
  </section>

  <!-- Counterwrap -->
  <p class="piece-label" style="left:473px; top:595px;">Counterwrap</p>
  <section class="piece counterwrap" style="left:267px; top:638px; width:618px; height:286px;">
    <div class="piece-bg" role="img" aria-label="Soft faceted background in mint green and peach tones"></div>
    <div class="brand" style="left:172px; top:20px; font-size:8px;">
      <span class="brand-mark" style="width:9px; height:9px;"></span>
      <span>Crestmoor Funding<br>Partners, LLC</span>
    </div>
    <div class="contact" style="left:381px; top:17px; font-size:11px;">555.018.4420<br>info@qvt7.net</div>
    <div class="band" style="top:63px; height:50px; font-size:25px;">WE CLOSE LOANS EXTREMELY FAST</div>
    <ul class="state-list" style="position:absolute; left:172px; top:128px; font-size:13.5px; line-height:17px;">
      <li>New Jersey</li><li>New York</li><li>Florida</li><li>Maryland</li>
      <li>Massachusetts</li><li>Connecticut</li><li>Pennsylvania</li><li>Virginia and D.C.</li>
    </ul>
    <div class="stat-number" style="left:359px; top:128px; font-size:35px;">725+</div>
    <div class="stat-label" style="left:363px; top:170px; width:80px; text-align:right; font-size:10px;">Project<br>Funded</div>
    <div class="stat-number" style="left:304px; top:200px; font-size:35px;">170 MM</div>
    <div class="stat-label" style="left:363px; top:246px; width:80px; text-align:right; font-size:10px;">Loans<br>Made</div>
  </section>

</body>
</html>
```